Sales Process

I need a card/page to hand out to my new clients that gives them an over view of our sales process start to finish. Along with 3 points that set us apart from all other competition.
The attached file is my first attempt with other ideas so give your suggestions.
Check out my website to get an idea of who we are. www.brindlefernyards.com

```html
<!DOCTYPE html>
<html lang="en">
<head>
<meta charset="utf-8">
<title>Brindlefern Yards – Sales Process</title>
<link href="https://fonts.googleapis.com/css2?family=Open+Sans:ital,wght@0,400;0,700;1,300&display=swap" rel="stylesheet">
<style>
  :root {
    --backdrop: #565556;
    --card-light: #f7f7f7;
    --card-edge: #e1e2e4;
    --ink: #1f1f24;
    --track-dark: #545456;
    --green: #8dc63f;
    --ring: #e4e5e7;
    --white: #ffffff;
    --orange: #eea52a;
    --sun: #f7c61a;
  }
  * { margin: 0; padding: 0; box-sizing: border-box; }
  html, body {
    width: 1200px; height: 928px; overflow: hidden;
    background: var(--backdrop);
    font-family: "Open Sans", Arial, sans-serif;
    color: var(--ink);
  }
  .page { position: relative; width: 1200px; height: 928px; }
  .card {
    position: absolute; left: 67px; top: 87px; width: 1066px; height: 754px;
    background: radial-gradient(ellipse at 50% 45%, var(--card-light) 0%, #eeeff0 55%, var(--card-edge) 100%);
    box-shadow: 0 4px 14px rgba(0,0,0,.35);
  }
  .process-art { position: absolute; left: 0; top: 0; width: 1200px; height: 928px; }
  .benefits {
    position: absolute; left: 106px; top: 136px;
    list-style: none; font-size: 16.5px; line-height: 30.4px;
  }
  .benefits li::before { content: "•"; display: inline-block; width: 16.5px; font-size: 13px; }
  .step-label {
    position: absolute; font-weight: 700; font-size: 20.5px; line-height: 24.3px;
    text-transform: uppercase; letter-spacing: .2px;
  }
  .step-initial { left: 131px; top: 474px; }
  .step-site { left: 389px; top: 677px; }
  .step-design { left: 454px; top: 324px; }
  .step-install { left: 710px; top: 544px; }
  .step-complete { left: 775px; top: 134px; font-size: 27px; line-height: 30.5px; }
  .step-complete .accent { color: var(--green); }
  .brand {
    position: absolute; left: 790px; top: 718px; width: 300px;
    display: flex; align-items: center; gap: 10px; white-space: nowrap;
  }
  .brand-dot { flex: none; width: 22px; height: 22px; border-radius: 50%; background: var(--green); }
  .brand-name { font-weight: 700; font-size: 25px; color: var(--track-dark); letter-spacing: .3px; }
  .tagline {
    position: absolute; right: 116px; top: 806px;
    font-style: italic; font-weight: 300; font-size: 15px; color: #3a3a3d;
  }
  .badge-num { font-family: "Open Sans", Arial, sans-serif; font-weight: 700; font-size: 44px; fill: var(--ink); }
</style>
</head>
<body>
<div class="page">
  <div class="card"></div>

  <svg class="process-art" viewBox="0 0 2184 1689" width="1200" height="928">
    <g class="track" fill="none" stroke-width="72">
      <path stroke="var(--green)" d="M246,1283 A165 165 0 0 0 536,1244"/>
      <path stroke="var(--track-dark)" d="M536,1244 A165 165 0 0 0 546,1188 C546,1000 580,896 673,896 C753.25,896 812.7,1001.2 884.6,1053.8"/>
      <path stroke="var(--green)" d="M884.6,1053.8 C908.6,1071.3 934,1083 962,1083 C1026,1083 1065.5,1049.75 1086.5,1004"/>
      <path stroke="var(--track-dark)" d="M1086.5,1004 C1107.5,958.25 1110,900 1100,850 C1070,700 1150,627 1255,627 C1348.75,627 1394.7,733.3 1465,786.5"/>
      <path stroke="var(--green)" d="M1465,786.5 C1488.4,804.2 1514.5,816 1546,816 C1680,816 1720,720 1720,650 C1720,560 1660,500 1710,435"/>
    </g>

    <g class="leaders" fill="none" stroke-width="3">
      <path stroke="var(--green)" d="M206,898 V1187 H262"/>
      <circle stroke="var(--green)" cx="206" cy="885" r="13" fill="var(--white)"/>
      <path stroke="var(--green)" d="M793,627 V864 H852"/>
      <circle stroke="var(--green)" cx="793" cy="614" r="13" fill="var(--white)"/>
      <path stroke="var(--green)" d="M1378,283 V597 H1437"/>
      <circle stroke="var(--green)" cx="1378" cy="270" r="13" fill="var(--white)"/>
      <path stroke="var(--track-dark)" d="M676,1180 V1413 H738"/>
      <circle stroke="var(--track-dark)" cx="751" cy="1413" r="13" fill="var(--white)"/>
      <path stroke="var(--track-dark)" d="M1256,910 V1143 H1318"/>
      <circle stroke="var(--track-dark)" cx="1332" cy="1143" r="13" fill="var(--white)"/>
    </g>

    <g class="stops">
      <circle cx="381" cy="1188" r="132" fill="var(--ring)"/>
      <circle cx="381" cy="1188" r="117" fill="var(--white)"/>
      <circle cx="673" cy="1061" r="132" fill="var(--ring)"/>
      <circle cx="673" cy="1061" r="117" fill="var(--white)"/>
      <circle cx="962" cy="918" r="132" fill="var(--ring)"/>
      <circle cx="962" cy="918" r="117" fill="var(--white)"/>
      <circle cx="1255" cy="792" r="132" fill="var(--ring)"/>
      <circle cx="1255" cy="792" r="117" fill="var(--white)"/>
      <circle cx="1546" cy="651" r="118" fill="var(--orange)"/>
    </g>

    <g class="icons">
      <rect role="img" aria-label="Support agent with headset icon" x="330" y="1125" width="98" height="120" rx="22" fill="var(--green)"/>
      <rect role="img" aria-label="Team meeting discussion icon" x="610" y="995" width="122" height="120" rx="20" fill="var(--track-dark)"/>
      <rect role="img" aria-label="Document with pencil icon" x="918" y="855" width="122" height="123" rx="14" fill="var(--green)"/>
      <rect role="img" aria-label="Construction hard hat with gear icon" x="1195" y="717" width="120" height="135" rx="24" fill="var(--track-dark)"/>
      <circle role="img" aria-label="Delighted smiling emoji" cx="1546" cy="651" r="80" fill="var(--sun)"/>
    </g>

    <g class="badges" stroke-width="8">
      <circle cx="443" cy="1383" r="50" fill="var(--white)" stroke="var(--green)"/>
      <text class="badge-num" x="443" y="1399" text-anchor="middle">01</text>
      <circle cx="572" cy="882" r="50" fill="var(--white)" stroke="var(--track-dark)"/>
      <text class="badge-num" x="572" y="898" text-anchor="middle">02</text>
      <circle cx="1052" cy="1110" r="50" fill="var(--white)" stroke="var(--green)"/>
      <text class="badge-num" x="1052" y="1126" text-anchor="middle">03</text>
      <circle cx="1155" cy="608" r="50" fill="var(--white)" stroke="var(--track-dark)"/>
      <text class="badge-num" x="1155" y="624" text-anchor="middle">04</text>
      <circle cx="1634" cy="843" r="50" fill="var(--white)" stroke="var(--green)"/>
      <text class="badge-num" x="1634" y="859" text-anchor="middle">05</text>
    </g>
  </svg>

  <ul class="benefits">
    <li>Lorem ipsum dolor sit amet, consectetur adipiscing elit, sed do</li>
    <li>Lorem ipsum dolor sit amet, consectetur adipiscing elit,</li>
    <li>Lorem ipsum dolor sit amet, consectetur adipiscing elit, sed do</li>
  </ul>

  <p class="step-label step-initial">Initial<br>call.<br>Can we<br>help?</p>
  <p class="step-label step-site">Site visit,<br>discuss,<br>plan,visit</p>
  <p class="step-label step-design">Design<br>proposal</p>
  <p class="step-label step-install">Installation<br>construction</p>
  <p class="step-label step-complete"><span class="accent">Complete</span><br>Kickback + relay with<br>smile on your face</p>

  <div class="brand">
    <span class="brand-dot"></span>
    <span class="brand-name">Brindlefern Yards</span>
  </div>
  <p class="tagline">Creating Exceptional Outdoor Living Spaces</p>
</div>
</body>
</html>
```